Now Leasing Banner

Looking for a banner that says the following information approx 4' x 30'

Now Leasing Maplewood Terrace 925-318-6054

Target Market(s)

Drive by traffic

Industry/Entity Type

Residential property management

Requirements
Must have
• Clear and readable from a distance

```html
<!DOCTYPE html>
<html lang="en">
<head>
<meta charset="utf-8">
<title>Now Leasing – Maplewood Terrace</title>
<link rel="stylesheet" href="https://fonts.googleapis.com/css2?family=Oswald:wght@300&family=Libre+Baskerville:wght@700&family=Playfair+Display:wght@900&display=swap">
<style>
  :root {
    --backdrop: #939396;
    --white: #ffffff;
    --gold-light: #b3921f;
    --gold-mid: #a3851e;
    --bronze-dark: #6e4f0c;
    --bronze-deep: #140803;
    --cream: #e4d092;
    --phone: #86672f;
    --glow: #f4e3a4;
  }
  html, body {
    margin: 0;
    width: 1200px;
    height: 281px;
    overflow: hidden;
    background: var(--backdrop);
  }
  .banner { display: block; width: 1200px; height: 281px; }
  .leasing-text {
    font-family: "Oswald", "Arial Narrow", sans-serif;
    font-weight: 300;
    fill: var(--cream);
  }
  .property-name {
    font-family: "Libre Baskerville", Georgia, serif;
    font-weight: 700;
    fill: var(--white);
  }
  .phone-number {
    font-family: "Playfair Display", Georgia, serif;
    font-weight: 900;
    fill: var(--phone);
  }
  .rule { stroke: var(--white); stroke-width: 2; }
</style>
</head>
<body>
<svg class="banner" viewBox="0 0 1200 281" xmlns="http://www.w3.org/2000/svg" aria-label="Now Leasing – Maplewood Terrace – 925-318-6054">
  <defs>
    <linearGradient id="panelGold" x1="0" y1="0" x2="1" y2="0">
      <stop offset="0" stop-color="#a88e20"/>
      <stop offset="1" stop-color="#9a7c18"/>
    </linearGradient>
    <linearGradient id="shadowFade" x1="0" y1="0" x2="0" y2="1">
      <stop offset="0" stop-color="var(--bronze-deep)"/>
      <stop offset="0.55" stop-color="#2a1403"/>
      <stop offset="1" stop-color="#6a4006"/>
    </linearGradient>
    <linearGradient id="bandGold" x1="0" y1="0" x2="1" y2="0">
      <stop offset="0" stop-color="#7a5c0c"/>
      <stop offset="1" stop-color="#b88a1c"/>
    </linearGradient>
    <linearGradient id="bandShadow" x1="0" y1="0" x2="0" y2="1">
      <stop offset="0" stop-color="#1e1004"/>
      <stop offset="1" stop-color="#7a5810"/>
    </linearGradient>
    <linearGradient id="glowLine" x1="0" y1="0" x2="1" y2="0">
      <stop offset="0" stop-color="var(--glow)" stop-opacity="0"/>
      <stop offset="0.5" stop-color="var(--glow)"/>
      <stop offset="1" stop-color="var(--glow)" stop-opacity="0"/>
    </linearGradient>
  </defs>

  <!-- white sign board -->
  <rect class="board" x="69.5" y="69.5" width="1061" height="141" fill="var(--white)"/>

  <!-- heading band -->
  <path class="title-band" d="M516 69.5 H1130.5 V127 H533 Q528 96 516 69.5 Z" fill="url(#bandGold)"/>
  <polygon class="title-band-shadow" points="545,96 610,96 640,83 1045,83 1060,98 1080,98 1105,118 1105,127 576,127" fill="url(#bandShadow)"/>
  <rect class="title-band-glow" x="640" y="125" width="280" height="2" fill="url(#glowLine)"/>
  <line class="rule" x1="545" y1="95" x2="593" y2="95"/>
  <line class="rule" x1="1062" y1="95" x2="1110" y2="95"/>
  <text class="property-name" x="827" y="111" text-anchor="middle" font-size="36" textLength="450" lengthAdjust="spacingAndGlyphs">MAPLEWOOD TERRACE</text>

  <!-- now leasing panel -->
  <path class="leasing-panel" d="M78 78 H514 Q540 140 507 202 H78 Z" fill="url(#panelGold)"/>
  <polygon class="leasing-shadow" points="96,98 112,95 507,95 522,140 508,200 110,200 96,185" fill="url(#shadowFade)"/>
  <text class="leasing-text" x="92" y="185" font-size="124" textLength="412" lengthAdjust="spacingAndGlyphs">NOW LEASING</text>

  <!-- phone number -->
  <text class="phone-number" x="555" y="196" font-size="78" textLength="544" lengthAdjust="spacingAndGlyphs">925-318-6054</text>
</svg>
</body>
</html>
```